TAILORED EYECARE AND EYEWEAR
Tailor made for you
We Care About Your Eyecare
Harwell Optometrists is a leading professional Opticians whose focus is on clinical care first and foremost using state of the are equipment followed by supplying design led spectacles and contact lenses. Our website is www.halvornsight.co.uk.
We are looking to have a postcard designed which will market the idea in requirements, this also has to have a poster to match which will be displayed in the store.
Health
Our target audience is adults aged 40 years+, our ethos is about patient care. The practice is both professional, clinical and design led. We must communicate the professionalism, simplicity and care. The Postcard will be personalised, obviously the poster will not.
A postcard which is A5 in size (please see the attached PDF for sizing and what areas to leave blank on the reverse for the address etc.) On the front if using a bleed this needs to be 3mm all round. To make it really tailored we would like to include the patients name on the front, this could be in any true type font as long as you supply a copy of the font, so it really can match in with the design. The Posters we require will be based upon the postcard and can be the same but 2 different sizes one is 60" x 40" portrait and the other 30" x 20" portrait. These all need to be CMYK and at 300DPI.
Postcard size information
Company Logo
Contact Details
Design Brief
Postcard Back Text
Postcard Front Text updated 09-09-11
Optometrist of the year logo
Premium Lens Practice Logo
Tailors Dummy

```html
<!DOCTYPE html>
<html lang="en">
<head>
<meta charset="utf-8">
<title>Harwell Optometrists – Tailored Eyecare and Eyewear</title>
<link rel="stylesheet" href="https://fonts.googleapis.com/css2?family=Didact+Gothic&display=swap">
<style>
  :root {
    --paper: #ffffff;
    --ink: #3a3a3c;
    --brand: #1f3a63;
    --photo-light: #f6ece5;
    --photo-mid: #ecd3c2;
    --photo-deep: #dbb39b;
  }
  html, body {
    margin: 0;
    padding: 0;
    overflow: hidden;
    background: var(--paper);
  }
  .postcard {
    position: relative;
    width: 1200px;
    height: 835px;
    background: var(--paper);
    overflow: hidden;
    font-family: "Didact Gothic", "Century Gothic", sans-serif;
    color: var(--ink);
  }
  .hero-photo {
    position: absolute;
    left: 0;
    top: 0;
    width: 620px;
    height: 620px;
  }
  .message {
    position: absolute;
    text-align: center;
    text-transform: uppercase;
    transform: translate(-50%, -50%) rotate(-24deg);
    white-space: nowrap;
  }
  .headline {
    left: 782px;
    top: 338px;
    margin: 0;
    font-weight: 400;
    font-size: 52px;
    line-height: 1.2;
    letter-spacing: 1px;
  }
  .body-copy {
    left: 875px;
    top: 592px;
    font-size: 23px;
    line-height: 1.3;
    letter-spacing: 0.5px;
  }
  .body-copy p {
    margin: 0 0 28px;
  }
  .body-copy p:last-child {
    margin-bottom: 0;
  }
  .brand {
    position: absolute;
    left: 100px;
    top: 725px;
    color: var(--brand);
    text-align: center;
    line-height: 1;
  }
  .brand-name {
    display: block;
    font-size: 62px;
  }
  .brand-tag {
    display: block;
    margin-top: 8px;
    font-size: 25px;
    letter-spacing: 4px;
  }
</style>
</head>
<body>
  <main class="postcard">
    <svg class="hero-photo" viewBox="0 0 620 620" role="img" aria-label="Photograph of a smiling woman peeking through torn white paper">
      <defs>
        <radialGradient id="photo-tone" cx="0.28" cy="0.3" r="0.8">
          <stop offset="0" stop-color="var(--photo-light)"/>
          <stop offset="0.55" stop-color="var(--photo-mid)"/>
          <stop offset="1" stop-color="var(--photo-deep)"/>
        </radialGradient>
        <filter id="soft-edge" x="-5%" y="-5%" width="110%" height="110%">
          <feGaussianBlur stdDeviation="6"/>
        </filter>
      </defs>
      <path d="M0,0 H560 C548,170 525,290 440,390 C350,490 210,545 0,565 Z" fill="url(#photo-tone)" filter="url(#soft-edge)"/>
    </svg>

    <h1 class="message headline">Does your optician treat<br>you like a number?</h1>

    <div class="message body-copy">
      <p>We don't, we listen and tailor eyecare<br>and eyewear for your needs<br>that's why our patients keep coming back!</p>
      <p>So why not join them for that personal touch?</p>
      <p>Tailored eyecare and eyewear<br>at Harwell Optometrists</p>
    </div>

    <div class="brand">
      <span class="brand-name">Harwell</span>
      <span class="brand-tag">OPTOMETRISTS</span>
    </div>
  </main>
</body>
</html>
```